I need a cover for a brochure made

I need a cover for a brochure. The dimensions are 8.25 wide and 5.25 high... I also need a .25 inch bleed outside of those dimensions.

I need it to look like a vintage photo album cover. In big words, I would like it to say "Family". Above it in smaller words "To our Carrowmere Paddle" ... making it look like the words are gold inlay or something.

I would like it kind of in the style of some of the attached maybe. Just vintage looking.

```html
<!DOCTYPE html>
<html lang="en">
<head>
<meta charset="utf-8">
<title>Family – Brochure Cover</title>
<link rel="stylesheet" href="https://fonts.googleapis.com/css2?family=Berkshire+Swash&family=Great+Vibes&display=swap">
<style>
  :root {
    --page: #eaeaea;
    --cover-dark: #2b190b;
    --cover-brown: #45240b;
    --spine-line: #6b3a10;
    --gold-light: #f5d57a;
    --gold-mid: #e2b65a;
    --gold-deep: #b9802f;
    --ink-white: #ffffff;
  }
  * { margin: 0; padding: 0; box-sizing: border-box; }
  html, body {
    width: 1200px;
    height: 845px;
    overflow: hidden;
    background: var(--page);
  }
  .cover {
    position: absolute;
    left: 258px;
    top: 205px;
    width: 685px;
    height: 435px;
    background: var(--cover-dark);
    overflow: hidden;
  }
  .cover__panels {
    position: absolute;
    inset: 0;
    width: 100%;
    height: 100%;
  }
  .cover__ornament {
    position: absolute;
    width: 134px;
    height: 130px;
  }
  .cover__ornament--top-left {
    left: 68px;
    top: 3px;
  }
  .cover__ornament--bottom-right {
    right: 5px;
    bottom: 3px;
    transform: rotate(180deg);
  }
  .cover__dedication {
    position: absolute;
    left: 345px;
    top: 134px;
    width: 240px;
    text-align: center;
    font-family: "Berkshire Swash", cursive;
    font-weight: 400;
    font-size: 21px;
    line-height: 1;
    color: var(--ink-white);
    white-space: nowrap;
  }
  .cover__title {
    position: absolute;
    left: 198px;
    top: 142px;
    width: 360px;
    text-align: center;
    font-family: "Great Vibes", cursive;
    font-weight: 400;
    font-size: 124px;
    line-height: 1.1;
    background: linear-gradient(90deg, var(--gold-deep) 0%, var(--gold-mid) 30%, var(--gold-light) 55%, var(--gold-mid) 80%, var(--gold-deep) 100%);
    -webkit-background-clip: text;
    background-clip: text;
    color: transparent;
    white-space: nowrap;
  }
</style>
</head>
<body>
  <main class="cover">
    <svg class="cover__panels" viewBox="0 0 685 435" aria-hidden="true">
      <defs>
        <linearGradient id="panel-left" x1="0" y1="0" x2="1" y2="1">
          <stop offset="0" stop-color="#432309"/>
          <stop offset="1" stop-color="#4a260b"/>
        </linearGradient>
        <linearGradient id="panel-right" x1="1" y1="0" x2="0" y2="1">
          <stop offset="0" stop-color="#3a1f0b"/>
          <stop offset="1" stop-color="#45240b"/>
        </linearGradient>
        <linearGradient id="rule-gold" x1="0" y1="0" x2="1" y2="0">
          <stop offset="0" stop-color="#b9802f" stop-opacity="0.3"/>
          <stop offset="0.5" stop-color="#f5d57a"/>
          <stop offset="1" stop-color="#b9802f" stop-opacity="0.3"/>
        </linearGradient>
      </defs>

      <path class="panel panel--left" fill="url(#panel-left)"
            d="M54 0 L349 0 C330 70 250 130 210 180 C185 210 178 240 175 260 C165 330 140 390 111 435 L54 435 Z"/>
      <path class="panel panel--right" fill="url(#panel-right)"
            d="M670 0 L685 0 L685 435 L440 435 C448 380 470 340 510 300 C560 250 590 200 605 135 C620 80 640 40 670 0 Z"/>

      <rect class="spine-rule" x="53" y="0" width="1.6" height="435" fill="#6b3a10"/>

      <g class="divider divider--top">
        <path d="M414 80.5 Q516 78.5 619 80.5 Q516 82.5 414 80.5 Z" fill="url(#rule-gold)"/>
        <path d="M514 72 L522 80.5 L514 89 L506 80.5 Z" fill="#f5d57a"/>
        <path d="M501 77.5 L504 80.5 L501 83.5 L498 80.5 Z M527 77.5 L530 80.5 L527 83.5 L524 80.5 Z" fill="#f5d57a"/>
        <path d="M494 79 L495.5 80.5 L494 82 L492.5 80.5 Z M534 79 L535.5 80.5 L534 82 L532.5 80.5 Z" fill="#e2b65a"/>
      </g>

      <g class="divider divider--bottom">
        <path d="M186 328 Q288 326 390 328 Q288 330 186 328 Z" fill="url(#rule-gold)"/>
        <path d="M287 319.5 L295 328 L287 336.5 L279 328 Z" fill="#f5d57a"/>
        <path d="M274 325 L277 328 L274 331 L271 328 Z M300 325 L303 328 L300 331 L297 328 Z" fill="#f5d57a"/>
        <path d="M267 326.5 L268.5 328 L267 329.5 L265.5 328 Z M307 326.5 L308.5 328 L307 329.5 L305.5 328 Z" fill="#e2b65a"/>
      </g>
    </svg>

    <svg class="cover__ornament cover__ornament--top-left" viewBox="0 0 134 130" role="img" aria-label="Gold filigree corner ornament">
      <defs>
        <radialGradient id="ornament-glow" cx="0.3" cy="0.3" r="0.75">
          <stop offset="0" stop-color="#e2b65a" stop-opacity="0.55"/>
          <stop offset="0.6" stop-color="#b9802f" stop-opacity="0.25"/>
          <stop offset="1" stop-color="#b9802f" stop-opacity="0"/>
        </radialGradient>
      </defs>
      <path d="M2 2 H130 Q70 14 40 40 Q14 66 2 126 Z" fill="url(#ornament-glow)"/>
    </svg>
    <svg class="cover__ornament cover__ornament--bottom-right" viewBox="0 0 134 130" role="img" aria-label="Gold filigree corner ornament">
      <defs>
        <radialGradient id="ornament-glow-b" cx="0.3" cy="0.3" r="0.75">
          <stop offset="0" stop-color="#e2b65a" stop-opacity="0.55"/>
          <stop offset="0.6" stop-color="#b9802f" stop-opacity="0.25"/>
          <stop offset="1" stop-color="#b9802f" stop-opacity="0"/>
        </radialGradient>
      </defs>
      <path d="M2 2 H130 Q70 14 40 40 Q14 66 2 126 Z" fill="url(#ornament-glow-b)"/>
    </svg>

    <p class="cover__dedication">To our Carrowmere Paddle</p>
    <h1 class="cover__title">Family</h1>
  </main>
</body>
</html>
```